Flyer

I am a qualified accountant and I need a flyer to promote my business when networking

My services include
Management Accounts, Financial Accounts, Day to Day Bookkeeping services, business start up assistance
I will produce and submit Self Assessment Tax Returns, Annual Accounts, VAT tax returns, Payroll and PAYE

I attach my business card design so that there is some continuity if you think it appropiate.

Size A3 is preferred, please.

Sorry, I mean't Size A5 is preferred.

A5 please

Free initial consultations and advice.                                   

Business

```html
<!DOCTYPE html>
<html lang="en">
<head>
<meta charset="utf-8">
<title>Clara Moss Accounting – Business Services Flyer</title>
<link href="https://fonts.googleapis.com/css2?family=Carlito:ital,wght@0,400;0,700;1,700&display=swap" rel="stylesheet">
<style>
  :root {
    --green-dark: #0d6b2c;
    --green-mid: #2a8a2f;
    --green-lime: #b6d334;
    --ink: #111111;
    --paper: #ffffff;
    --photo-blue: #c9d6e6;
    --photo-grey: #8fa1b5;
  }
  * { margin: 0; padding: 0; box-sizing: border-box; }
  html, body { width: 846px; height: 1200px; overflow: hidden; background: var(--paper); }
  .flyer {
    position: relative;
    width: 846px; height: 1200px;
    font-family: "Carlito", "Calibri", sans-serif;
    color: var(--ink);
    overflow: hidden;
  }
  .header-bands { position: absolute; left: 0; top: 0; width: 846px; height: 74px; }
  .photo { position: absolute; }
  .photo--desk {
    left: 23px; top: 118px; width: 386px; height: 233px;
    background: linear-gradient(135deg, #eef2f7 0%, var(--photo-blue) 55%, var(--photo-grey) 100%);
  }
  .photo--meeting {
    left: 436px; top: 885px; width: 410px; height: 238px;
    background: linear-gradient(120deg, #f3f5f8 0%, var(--photo-blue) 50%, #6f8db0 100%);
  }
  .icon-team {
    position: absolute; left: 159px; top: 378px; width: 144px; height: 137px;
    border-radius: 50%;
    background: radial-gradient(circle at 40% 40%, #7fb2e0 0%, #3b7a3f 60%, #e08a2a 100%);
  }
  .brand {
    position: absolute; left: 420px; top: 112px; width: 400px;
    text-align: center;
  }
  .brand__name {
    font-weight: 700; font-size: 47px; line-height: 62px; letter-spacing: 1.5px;
  }
  .brand__tagline {
    margin-top: 8px; font-size: 23px; letter-spacing: 0.5px;
  }
  .services-badge { position: absolute; left: 315px; top: 386px; width: 378px; height: 136px; }
  .services-badge__label {
    position: absolute; inset: 0;
    display: flex; flex-direction: column; align-items: center; justify-content: center;
    font-weight: 700; font-style: italic; font-size: 39px; line-height: 46px; letter-spacing: 1.5px;
  }
  .services {
    position: absolute; left: 62px; top: 535px; list-style: none;
    color: var(--green-dark);
    font-weight: 700; font-style: italic; font-size: 37px; line-height: 53px; letter-spacing: 1.2px;
    word-spacing: 4px;
  }
  .services li { position: relative; padding-left: 44px; }
  .services li svg { position: absolute; left: 0; top: 16px; width: 26px; height: 24px; }
  .footer {
    position: absolute; left: 0; top: 1145px; width: 846px; height: 55px;
    background: linear-gradient(90deg, var(--green-lime) 0%, var(--green-mid) 45%, var(--green-dark) 100%);
    display: flex; align-items: center; justify-content: center;
    font-weight: 700; font-size: 20px; letter-spacing: 0.3px;
  }
</style>
</head>
<body>
<div class="flyer">
  <svg class="header-bands" viewBox="0 0 846 74" aria-hidden="true">
    <rect x="0" y="0" width="846" height="30" fill="var(--green-dark)"/>
    <path d="M40 30 H846 V74 H0 V70 Q0 30 40 30 Z" fill="var(--green-lime)"/>
    <rect x="431" y="50" width="415" height="24" fill="var(--green-dark)"/>
  </svg>

  <div class="photo photo--desk" role="img" aria-label="Photo of hands using a calculator over financial papers"></div>

  <div class="brand">
    <div class="brand__name">CLARA MOSS<br>ACCOUNTING</div>
    <div class="brand__tagline">MAKING ACCOUNTS LOOK EASY</div>
  </div>

  <div class="icon-team" role="img" aria-label="Illustration of two business people with a gear"></div>

  <div class="services-badge">
    <svg width="378" height="136" viewBox="0 0 378 136" aria-hidden="true">
      <defs>
        <radialGradient id="badgeFill" cx="50%" cy="45%" r="60%">
          <stop offset="0%" stop-color="#d7ea7a"/>
          <stop offset="45%" stop-color="#6fb43a"/>
          <stop offset="100%" stop-color="#1f7a2c"/>
        </radialGradient>
      </defs>
      <ellipse cx="189" cy="68" rx="188" ry="67" fill="url(#badgeFill)"/>
    </svg>
    <div class="services-badge__label"><span>BUSINESS</span><span>SERVICES</span></div>
  </div>

  <ul class="services">
    <li><svg viewBox="0 0 26 24" aria-hidden="true"><path d="M2 13 L9 21 L24 2" fill="none" stroke="var(--green-dark)" stroke-width="3"/></svg>Management Accounts</li>
    <li><svg viewBox="0 0 26 24" aria-hidden="true"><path d="M2 13 L9 21 L24 2" fill="none" stroke="var(--green-dark)" stroke-width="3"/></svg>Financial Accounts</li>
    <li><svg viewBox="0 0 26 24" aria-hidden="true"><path d="M2 13 L9 21 L24 2" fill="none" stroke="var(--green-dark)" stroke-width="3"/></svg>Day to Day Book Keeping Services</li>
    <li><svg viewBox="0 0 26 24" aria-hidden="true"><path d="M2 13 L9 21 L24 2" fill="none" stroke="var(--green-dark)" stroke-width="3"/></svg>Business Start Up Assistance</li>
    <li><svg viewBox="0 0 26 24" aria-hidden="true"><path d="M2 13 L9 21 L24 2" fill="none" stroke="var(--green-dark)" stroke-width="3"/></svg>Can Produce And Submit Self<br>Assessment Tax Returns</li>
    <li><svg viewBox="0 0 26 24" aria-hidden="true"><path d="M2 13 L9 21 L24 2" fill="none" stroke="var(--green-dark)" stroke-width="3"/></svg>Annual Accounts</li>
    <li><svg viewBox="0 0 26 24" aria-hidden="true"><path d="M2 13 L9 21 L24 2" fill="none" stroke="var(--green-dark)" stroke-width="3"/></svg>VAT tax returns</li>
    <li><svg viewBox="0 0 26 24" aria-hidden="true"><path d="M2 13 L9 21 L24 2" fill="none" stroke="var(--green-dark)" stroke-width="3"/></svg>Payroll</li>
    <li><svg viewBox="0 0 26 24" aria-hidden="true"><path d="M2 13 L9 21 L24 2" fill="none" stroke="var(--green-dark)" stroke-width="3"/></svg>PAYE</li>
  </ul>

  <div class="photo photo--meeting" role="img" aria-label="Photo of colleagues reviewing printed charts with a pen"></div>

  <div class="footer">EMAIL: clara@claramossaccounting.com CONTACT # 07700 900123</div>
</div>
</body>
</html>
```